Energy Company needs a Business Card Design

We need a business card design for a new company based in Singapore called Tarn Energy. Tarn Energy is a producer of renewable energies largely for the biofuels market. Sourced entirely from sustainable resources, Tarn Energy aims to be a fully integrated oil company operating in 100% sustainable way. We would like to see designs that use the same colours as the attached file.

Industry/Entity Type

Business

```html
<!DOCTYPE html>
<html lang="en">
<head>
<meta charset="utf-8">
<title>Tarn Energy – Business Card</title>
<link rel="stylesheet" href="https://fonts.googleapis.com/css2?family=Mulish:wght@400;700&family=Questrial&display=swap">
<style>
  :root {
    --backdrop: #ececec;
    --card: #ffffff;
    --leaf-green: #7ab33a;
    --slate: #7d7d7d;
    --slate-dark: #6f6f6f;
    --text-grey: #8a8a8a;
  }
  * { box-sizing: border-box; margin: 0; padding: 0; }
  html, body { width: 1200px; height: 720px; overflow: hidden; }
  body {
    background: var(--backdrop);
    position: relative;
    font-family: "Questrial", sans-serif;
  }
  .card {
    position: absolute;
    top: 241px;
    width: 420px;
    height: 240px;
    background: var(--card);
    box-shadow: 0 1px 3px rgba(0,0,0,0.12);
  }
  .card--front { left: 147px; }
  .card--back { left: 633px; }

  /* Front */
  .front-brand {
    position: absolute;
    left: 0; right: 0;
    top: 78px;
    display: flex;
    justify-content: center;
    align-items: center;
    gap: 12px;
  }
  .brand-dot {
    width: 18px; height: 18px;
    border-radius: 50%;
    background: var(--leaf-green);
  }
  .front-brand .brand-name {
    font-family: "Questrial", sans-serif;
    font-size: 52px;
    color: var(--slate);
    letter-spacing: -0.5px;
    line-height: 1;
  }
  .tagline {
    position: absolute;
    left: 0; right: 0;
    top: 183px;
    text-align: center;
    font-size: 15px;
    color: var(--leaf-green);
  }

  /* Back */
  .holder {
    position: absolute;
    left: 21px;
    top: 66px;
  }
  .holder-name {
    font-family: "Mulish", sans-serif;
    font-weight: 700;
    font-size: 16px;
    color: var(--leaf-green);
    line-height: 1.1;
  }
  .holder-role {
    font-size: 13px;
    color: var(--text-grey);
    line-height: 1.2;
  }
  .contacts {
    position: absolute;
    left: 20px;
    top: 117px;
    list-style: none;
  }
  .contacts li {
    display: flex;
    align-items: center;
    height: 19px;
    font-size: 11.5px;
    color: var(--text-grey);
  }
  .contacts svg {
    width: 12px; height: 12px;
    margin-right: 7px;
    flex: none;
  }
  .back-brand {
    position: absolute;
    right: 21px;
    top: 100px;
    display: flex;
    align-items: center;
    gap: 8px;
  }
  .back-brand .brand-dot { width: 11px; height: 11px; }
  .back-brand .brand-name {
    font-size: 28px;
    color: var(--slate);
    line-height: 1;
  }
</style>
</head>
<body>
  <section class="card card--front" aria-label="Business card front">
    <div class="front-brand">
      <span class="brand-name">Tarn Energy</span>
      <span class="brand-dot"></span>
    </div>
    <p class="tagline">Energy for Biofuels Market</p>
  </section>

  <section class="card card--back" aria-label="Business card back">
    <div class="holder">
      <p class="holder-name">Lena Marsh</p>
      <p class="holder-role">CEO</p>
    </div>
    <ul class="contacts">
      <li>
        <svg viewBox="0 0 12 12" aria-hidden="true"><rect x="3" y="0.8" width="6" height="10.4" rx="1" fill="none" stroke="#7ab33a" stroke-width="1.2"/><line x1="5" y1="9.3" x2="7" y2="9.3" stroke="#7ab33a" stroke-width="1"/></svg>
        + 65 552 3190
      </li>
      <li>
        <svg viewBox="0 0 12 12" aria-hidden="true"><rect x="0.8" y="2.5" width="10.4" height="7" fill="#7ab33a"/><polyline points="0.8,2.5 6,6.6 11.2,2.5" fill="none" stroke="#fff" stroke-width="1"/></svg>
        hello@tarnenergy.com
      </li>
      <li>
        <svg viewBox="0 0 12 12" aria-hidden="true"><g fill="none" stroke="#7ab33a" stroke-width="1"><circle cx="6" cy="6" r="5.2"/><ellipse cx="6" cy="6" rx="2.3" ry="5.2"/><line x1="0.8" y1="6" x2="11.2" y2="6"/><line x1="1.6" y1="3.4" x2="10.4" y2="3.4"/><line x1="1.6" y1="8.6" x2="10.4" y2="8.6"/></g></svg>
        www.tarnenergy.com
      </li>
    </ul>
    <div class="back-brand">
      <span class="brand-name">Tarn Energy</span>
      <span class="brand-dot"></span>
    </div>
  </section>
</body>
</html>
```